Pet business needs a business card

Pet shop needs a business card. Like dark background and and debased look.

Meadowpaws
Lindenweg 47
B - 3280 Velmor
Belgium

www.meadowpaws-example.com
mail@meadowpaws-example.com
Phone +32478610927

I will ad a tagline shortly.

Industry/Entity Type

Shop

Font styles to use
Sans Serif

Requirements
Must have
• Must be possible to print the card debased. See example image.

```html
<!DOCTYPE html>
<html lang="en">
<head>
<meta charset="utf-8">
<title>Meadowpaws – Business Card</title>
<link rel="stylesheet" href="https://fonts.googleapis.com/css2?family=Didact+Gothic&display=swap">
<style>
  :root {
    --card-bg: #9c2a7d;
    --page-bg: #ffffff;
    --ink-cream: #f4ecc8;
    --ink-shadow: rgba(40, 20, 30, 0.55);
    --art-orange: #f39a3c;
    --art-grey: #6f6258;
  }
  * { margin: 0; padding: 0; box-sizing: border-box; }
  html, body {
    width: 1200px;
    height: 299px;
    overflow: hidden;
    background: var(--page-bg);
    font-family: "Didact Gothic", "Century Gothic", sans-serif;
  }
  .sheet {
    position: relative;
    width: 1200px;
    height: 299px;
  }
  .card {
    position: absolute;
    top: 0;
    height: 299px;
    background: var(--card-bg);
    color: var(--ink-cream);
  }
  .card--front { left: 0; width: 586px; }
  .card--back { left: 615px; width: 585px; }

  .mascot-art {
    position: absolute;
    left: 117px;
    top: 18px;
    width: 387px;
    height: 158px;
    background: linear-gradient(120deg, var(--art-orange) 0%, var(--art-orange) 55%, var(--art-grey) 100%);
    border-radius: 6px;
    opacity: 0.9;
  }
  .brand-name {
    position: absolute;
    color: var(--ink-cream);
    letter-spacing: 1px;
    text-shadow: none;
  }
  .card--front .brand-name {
    left: 117px;
    top: 175px;
    font-size: 38px;
  }
  .card--back .brand-name {
    left: 0;
    width: 585px;
    top: 64px;
    text-align: center;
    font-size: 30px;
  }
  .web-line {
    position: absolute;
    left: 16px;
    right: 10px;
    bottom: 18px;
    font-size: 13.5px;
    letter-spacing: 0.4px;
    white-space: nowrap;
    text-shadow: 1px 1px 0 var(--ink-shadow);
  }
  .phone {
    position: absolute;
    left: 0;
    width: 585px;
    top: 114px;
    text-align: center;
    font-size: 18px;
    letter-spacing: 0.8px;
    text-shadow: 1px 1px 0 var(--ink-shadow);
  }
  .address {
    position: absolute;
    left: 30px;
    top: 206px;
    font-style: normal;
    font-size: 21px;
    line-height: 29px;
    letter-spacing: 0.6px;
    text-shadow: 1px 1px 0 var(--ink-shadow);
  }
</style>
</head>
<body>
<main class="sheet">
  <section class="card card--front">
    <div class="mascot-art" role="img" aria-label="Illustration of a stylised running dog in orange and grey"></div>
    <div class="brand-name">Meadowpaws</div>
    <p class="web-line">Website : www.meadowpaws-example.com Email : mail@meadowpaws-example.com</p>
  </section>

  <section class="card card--back">
    <div class="brand-name">Meadowpaws</div>
    <p class="phone">Phone +32478610927</p>
    <address class="address">
      Lindenweg 47<br>
      B - 3280 Velmor<br>
      Belgium
    </address>
  </section>
</main>
</body>
</html>
```